Delvin & Associates - London New Letting and Property Management Company *

Delvin & Associates LTD is a new company based in London, and works with brand new residential property in the city centre.

We are aiming to have 1000 new properties a year.

We are looking for something modern and minimalistic :
Logo ,Monogram, Paper Head and Business Card.

Target Market(s)

Internation landlords

Industry/Entity Type

Real Estate

Logo Text

Delvin & Associates

Colors

Designer to choose colors to be used in the design.

Requirements
Nice to have
• A particular monogram with "DA"
Should not have
• Little House over the logo

```html
<!DOCTYPE html>
<html lang="en">
<head>
<meta charset="utf-8">
<title>Delvin &amp; Associates – Business Card</title>
<link rel="stylesheet" href="https://fonts.googleapis.com/css2?family=Lato:wght@300;400&display=swap">
<style>
  :root {
    --page: #ffffff;
    --ink: #0a0a0b;
    --paper: #ffffff;
    --band: #e6e7e8;
    --rule: #cfd0d2;
    --muted: #8a8a8a;
    --frame: #bdbdbd;
  }
  * { margin: 0; padding: 0; box-sizing: border-box; }
  html, body { width: 1200px; height: 1000px; overflow: hidden; background: var(--page); }
  body { position: relative; font-family: "Lato", sans-serif; color: var(--ink); }

  .card { position: absolute; box-shadow: 0 12px 40px rgba(0,0,0,0.18); }

  .card-front {
    left: 292px; top: 107px; width: 616px; height: 352px;
    background: var(--ink);
  }
  .front-mark {
    position: absolute; left: 220px; top: 110px; width: 173px; height: 129px;
    border: 2px solid var(--frame);
    display: flex; align-items: center; justify-content: center;
    color: var(--paper); font-size: 92px; font-weight: 400; letter-spacing: 2px;
  }

  .card-back {
    left: 296px; top: 498px; width: 619px; height: 377px;
    background: var(--paper);
  }
  .back-band {
    position: absolute; left: 0; top: 0; width: 100%; height: 160px;
    background: var(--band); border-bottom: 1px solid var(--rule);
  }
  .back-mark {
    position: absolute; left: 43px; top: 123px; width: 102px; height: 77px;
    background: var(--ink); color: var(--paper);
    display: flex; align-items: center; justify-content: center;
    font-size: 44px; font-weight: 400; letter-spacing: 1px;
  }
  .company-name {
    position: absolute; left: 187px; top: 142px;
    font-size: 41px; font-weight: 400; line-height: 1; white-space: nowrap;
  }
  .role {
    position: absolute; left: 187px; top: 192px;
    font-size: 16px; font-weight: 300; color: var(--muted);
  }
  .contacts { position: absolute; left: 123px; top: 248px; list-style: none; }
  .contacts li {
    display: flex; align-items: center; height: 37px;
    font-size: 19px; font-weight: 400;
  }
  .contacts .icon {
    width: 21px; height: 21px; background: var(--ink); margin-right: 12px;
    display: flex; align-items: center; justify-content: center;
  }
</style>
</head>
<body>
  <section class="card card-front">
    <div class="front-mark">DA</div>
  </section>

  <section class="card card-back">
    <div class="back-band"></div>
    <div class="back-mark">DA</div>
    <h1 class="company-name">Delvin &amp; Associates</h1>
    <p class="role">Real Estate Agent</p>
    <ul class="contacts">
      <li>
        <span class="icon"><svg width="13" height="13" viewBox="0 0 24 24"><path fill="#fff" d="M6.6 10.8a15 15 0 0 0 6.6 6.6l2.2-2.2c.3-.3.7-.4 1-.2 1.1.4 2.3.6 3.6.6.6 0 1 .4 1 1V20c0 .6-.4 1-1 1A17 17 0 0 1 3 4c0-.6.4-1 1-1h3.5c.6 0 1 .4 1 1 0 1.3.2 2.5.6 3.6.1.3 0 .7-.2 1z"/></svg></span>
        +12 345 7777
      </li>
      <li>
        <span class="icon"><svg width="13" height="10" viewBox="0 0 26 20"><rect x="1" y="1" width="24" height="18" fill="none" stroke="#fff" stroke-width="2"/><path d="M1 1l12 10L25 1" fill="none" stroke="#fff" stroke-width="2"/></svg></span>
        info@delvinassociates.com
      </li>
      <li>
        <span class="icon"><svg width="13" height="13" viewBox="0 0 24 24"><circle cx="12" cy="12" r="10" fill="none" stroke="#fff" stroke-width="2"/><path d="M2 12h20M12 2c3 3 3 17 0 20M12 2c-3 3-3 17 0 20" fill="none" stroke="#fff" stroke-width="1.6"/></svg></span>
        delvinassociates.com
      </li>
    </ul>
  </section>
</body>
</html>
```